Cosmetic Jar (Lid Only) Packaging Design Project

UPDATE: I realize that the links I provided show products w/ packaging v. unlike my own, and that does limit you a lot design wise, so here are some links of logos/lid designs I like for v. similar jars:
I like how this one tells the brand and the product: http://www.skinvaultshop.example/product_Loose+Powder+-+Dune_34162.htm
http://www.belmarest.example/skin-foundation-mineral-makeup-spf-15-P296207?skuId=1353192
http://www.belmarest.example/wild-rose-mineral-foundation-P277218?skuId=1440957
http://www.plumvelle.example/
http://www.tovanbloom.example/assets/2012/11/07/eyes-banner-1.jpg
Also, black and white are fine for the colors, as the bright pink may look less professional.

*I've added two pics w/o the labels on the jar lids in case that helps!

*I'm hoping to see something that maybe has a graphic design that covers much of the lid, or is a bit abstract. I want people to think pretty and luxury when they see it. Please keep the submissions coming and I'll do my best to provide helpful feedback. Thank you all!

I need a package design for a heat-stamp (so for a die to be made and used for stamping the makeup jar's lid) for the plastic makeup jars of a natural, luxury makeup line. The jars will not have individual boxes, they will likely be placed in an organza or other fabric bag with the other products to reduce packaging.

I am currently launching gentle HUEWORK on Fundmarble, so for more images and info. please check it out here: www.fundmarble.example/gentlehuework

Name: gentle HUEWORK

The line’s core product is a three part makeup process (the three products being smooth, color and set) and all together the three part set is called the trifecta. All products use only natural and cosmetic-grade mineral ingredients. The packaging design is for the jar lids of the two products: color and set.

Key Distinctions:
-gentle HUEWORK’s products are free from Titanium Dioxide, Zinc Oxide and Micas. Titanium Dioxide and Micas have been linked to cancer, Zinc Oxide has been linked to respiratory and reproductive toxicity, but it is nearly impossible to find a department store, natural or mineral makeup that is free of all three of these ingredients.
-gentle HUEWORK’s three part process, our trifecta, begins with the product called smooth, it is like a primer in that it smooths and evens the skin’s surface for color makeup application, but different in that it contains only beneficial ingredients (nearly all other makeup primers contain a base of silicone, glycerin or polyethylene). smooth is made with only three key ingredients: mango butter, sea buckthorn oil, jojoba esters, and then also contains essential oils and vitamin e oil to prevent oxidation.
-gentle HUEWORK’s color and set products are lightweight, blendable, buildable, and contain copious amounts of pearl powder **so the products are not vegan** the pearl powder is rich in calcium and protein, making it beneficial to the skin, as protein and calcium loss contribute to aging.

Mission:
To do to the makeup industry in 2013 what PlainQuartzes did in 1995 via HBN: to make and educate people about safer cosmetics. Before then foundations were not powder, they were cream or liquid. PlainQuartzes stripped it down to just the powders, ditching the petro-chems, parabens and phthalates. gentle HUEWORK adds in only essential, nourishing oils and butters like mango and prized sea buckthorn, but then strips down the mineral components (color and set) to only the most essential and safest powdered mineral makeup ingredients, adding in only high quality ingredients like pearl powder and arrowroot starch (a rice powder alternative, since rice is found to be contaminated with arsenic). Mineral makeup made cosmetics safer, now it’s time to make natural and mineral makeups safer.

Packaging:
I would like to keep the same jars for color and set that are currently used, a 25g clear jar and a 20g clear jar with a black shiny lid. If I had to change the smaller jar with the black shiny lid, it could match the clear jar, but the clear jar with the wider lid is necessary for at least the color product, though it could also be used for set.

Dimensions:
-Clear 25g color jar: 2.75" Diameter; 5/8" tall, 70 mm Diameter x 15 mm tall
-Black Lidded 20g set jar: 2" Diameter; 3/4" tall, 50 mm Diameter x 19 mm tall

Some Designs I Like:
I actually prefer the gold and silver in this case, but am not sure it would translate for my brand http://manyhuesblog.example/2011/10/11/stallmart-cosmetic-packaging/
I probably won't have boxes for the products, but the graphics of this are lovely http://clipboardly.example/pin/23925441740262945/
Again, not planning to have boxes for each indiv. product, but I like that Tovan Bloom uses the bird to represent their line, the idea of a symbol that can be identified as a brand http://www.boxcritique.example/blog/2010/9/8/tovan-bloom.html
Absolutely beautiful, but I don't have the option of square packaging http://tidyobjectsdaily.examplelog.example/post/5975797800/submission-merlow-and-daine-make-up-packaging-by
A random one, but love the look and feel http://clipboardly.example/pin/267190190363659062/
Updates

I've changed the project to Payment Guaranteed, please check it out, it's for the jar lid design only, so could be an easy $220 for most of you based on what I've seen! There is a lot, lot, lot of talent out there, please help me make natural, safer, healthier makeup the norm by submitting your awesome designs for the makeup jar lids! Thanks so much!!

I realize that the links I provided show products w/ packaging v. unlike my own, and that does limit you a lot design wise, so here are some links of logos/lid designs I like for v. similar jars:

I like that this one identifies the brand and the product, in this case the products would be "color" and "set"
http://www.skinvaultshop.example/product_Loose+Powder+-+Dune_34162.htm

Thank you all so much for your beautiful designs!
After much thought and seeing a lot of variance, I think that what will go best w/ the existing website (www.gentlehuework.example) and logo is something similar to this:
http://img.quillhost.example/-VQrHTZdUVyA/T58YzVNofBI/AAAAAAAADsA/rQtBatrU5Tg/s1600/Pavlin+Wild+Rose+Mineral+Setting+Powder.JPG

I would love to see your take on this, the Pavlin part could be the gentle HUEWORK logo (with the flower, but without smooth.color.set.)
The part that says: "wild rose setting powder, rose sauvage . . ." could say "handmade with love in the USA"
And the part that says: "mineral . . . fixatrice" could say smooth color set (on two or three lines) and the words color and set could be bolded on their own lids
And I think that the font would be great in white on the black lid and in black or white on the clear lid.

Thank you all so much!!
Marisol

Target Market(s)

women ages 18-65

Industry/Entity Type

Graphic Design

Requirements
Must have
• A one color design that can be (heat/foil) stamped onto the plastic makeup jar lids, that will show up on both the clear and black plastic lids.
It MUST say the brand name, or otherwise indicate it, but does not need to say the product (color or set) or anything else, but can if that helps.
I have an existing logo, but am open to alterations of it (i.e. am open to changes to the logo if they are necessary for the packaging aesthetic to be just right). I like the black with bright pink (fd33ab) for the brand, but am open to other suggestions.
I currently use waterproof, polyester laser printed labels for the jar tops, but don’t think those will look professional enough for the major beauty magazines. If you feel that you have a design that will only work with a label, I may consider it, but am leaning towards a design that can be printed/stamped directly onto the plastic jars. I am planning to have the lids foil/heat stamped though I prefer the matte colors to the metallics.

```html
<!DOCTYPE html>
<html lang="en">
<head>
<meta charset="utf-8">
<title>gentle HUEWORK — lid stamp studies</title>
<link href="https://fonts.googleapis.com/css2?family=Open+Sans:wght@400;600;700&display=swap" rel="stylesheet">
<style>
  :root {
    --lid-black: #000000;
    --lid-clear: #f9f9f9;
    --divider: #6b6868;
    --brand-pink: #fd33ab;
    --brand-pink-soft: #f566bd;
    --ink-light: #c9c9c9;
    --ink-white: #ffffff;
    --ink-dark: #333333;
    --rule-light: #b8b8b8;
    --rule-dark: #222222;
  }
  * { margin: 0; padding: 0; box-sizing: border-box; }
  html, body { width: 1200px; height: 3008px; overflow: hidden; background: var(--lid-clear); }
  body { font-family: "Open Sans", Arial, sans-serif; }

  .sheet { width: 1200px; height: 3008px; display: flex; flex-direction: column; }
  .study { height: 596px; display: flex; flex: none; }
  .study + .study { border-top: 7px solid var(--divider); height: 603px; }
  .lid { position: relative; height: 100%; overflow: hidden; }
  .lid--black { width: 655px; background: var(--lid-black); color: var(--ink-light); }
  .lid--clear { width: 545px; background: var(--lid-clear); color: var(--ink-dark); }

  .el { position: absolute; line-height: 1; white-space: nowrap; }

  .brand { position: absolute; line-height: 0.9; color: var(--brand-pink); font-size: 32px; }
  .brand__small { display: block; font-weight: 400; text-transform: lowercase; }
  .brand__caps { display: block; font-weight: 400; letter-spacing: 0.5px; }
  .lid--clear .brand--soft { color: var(--brand-pink-soft); }
  .brand--right { text-align: right; }

  .vrule { position: absolute; width: 3px; background: var(--rule-light); }
  .lid--clear .vrule { background: var(--rule-dark); width: 2px; }
  .hrule { position: absolute; height: 4px; background: var(--rule-light); }
  .lid--clear .hrule { background: var(--rule-dark); height: 3px; }

  .tagline { position: absolute; font-weight: 600; line-height: 1.3; white-space: nowrap; }
  .lid--black .tagline { color: var(--ink-white); }
  .tagline--center { text-align: center; }

  .bold { font-weight: 700; }
  .regular { font-weight: 400; }
</style>
</head>
<body>
<main class="sheet">

  <!-- Study 1: stacked product names beside a vertical rule -->
  <section class="study">
    <div class="lid lid--black">
      <div class="brand" style="left:120px; top:244px;"><span class="brand__small">gentle</span><span class="brand__caps">HUEWORK</span></div>
      <div class="vrule" style="left:308px; top:90px; height:405px;"></div>
      <p class="tagline" style="left:325px; top:148px; font-size:22px;">handmade with love<br>in the USA</p>
      <p class="el regular" style="left:322px; top:215px; font-size:46px;">SMOOTH</p>
      <p class="el bold" style="left:322px; top:259px; font-size:55px;">COLOR</p>
      <p class="el bold" style="left:318px; top:300px; font-size:108px;">SET</p>
    </div>
    <div class="lid lid--clear">
      <div class="brand" style="left:55px; top:255px;"><span class="brand__small">gentle</span><span class="brand__caps">HUEWORK</span></div>
      <div class="vrule" style="left:237px; top:90px; height:410px;"></div>
      <p class="tagline" style="left:252px; top:155px; font-size:21px;">handmade with love<br>in the USA</p>
      <p class="el regular" style="left:252px; top:232px; font-size:46px;">SMOOTH</p>
      <p class="el bold" style="left:252px; top:267px; font-size:60px;">COLOR</p>
      <p class="el regular" style="left:252px; top:325px; font-size:46px;">SET</p>
    </div>
  </section>

  <!-- Study 2: compact names with centred tagline -->
  <section class="study">
    <div class="lid lid--black">
      <div class="brand" style="left:118px; top:238px;"><span class="brand__small">gentle</span><span class="brand__caps">HUEWORK</span></div>
      <div class="vrule" style="left:304px; top:83px; height:400px;"></div>
      <p class="el bold" style="left:330px; top:218px; font-size:27px;">SMOOTH</p>
      <p class="el regular" style="left:330px; top:251px; font-size:27px;">COLOR <span class="bold">SET</span></p>
      <p class="tagline tagline--center" style="left:318px; top:282px; width:210px; font-size:20px;">handmade with love<br>in the USA</p>
    </div>
    <div class="lid lid--clear">
      <div class="brand brand--soft" style="left:62px; top:238px;"><span class="brand__small">gentle</span><span class="brand__caps">HUEWORK</span></div>
      <div class="vrule" style="left:237px; top:80px; height:405px;"></div>
      <p class="el bold" style="left:268px; top:216px; font-size:30px;">SMOOTH</p>
      <p class="el bold" style="left:268px; top:246px; font-size:40px;">COLOR <span style="font-size:28px;">SET</span></p>
      <p class="tagline tagline--center" style="left:256px; top:288px; width:220px; font-size:21px;">handmade with love<br>in the USA</p>
    </div>
  </section>

  <!-- Study 3: brand top right, oversized SET -->
  <section class="study">
    <div class="lid lid--black">
      <div class="brand brand--right" style="left:372px; top:95px;"><span class="brand__small">gentle</span><span class="brand__caps">HUEWORK</span></div>
      <p class="tagline" style="left:160px; top:191px; font-size:22px;">handmade with love in the USA</p>
      <p class="el regular" style="left:158px; top:215px; font-size:46px;">SMOOTH</p>
      <p class="el regular" style="left:158px; top:262px; font-size:52px;">COLOR</p>
      <p class="el bold" style="left:152px; top:300px; font-size:108px;">SET</p>
    </div>
    <div class="lid lid--clear">
      <div class="brand brand--right" style="left:330px; top:95px;"><span class="brand__small">gentle</span><span class="brand__caps">HUEWORK</span></div>
      <p class="tagline" style="left:117px; top:191px; font-size:22px;">handmade with love in the USA</p>
      <p class="el regular" style="left:115px; top:215px; font-size:46px;">SMOOTH</p>
      <p class="el regular" style="left:115px; top:262px; font-size:52px;">COLOR</p>
      <p class="el bold" style="left:109px; top:300px; font-size:108px;">SET</p>
    </div>
  </section>

  <!-- Study 4: horizontal rule, names set in a row -->
  <section class="study">
    <div class="lid lid--black">
      <div class="brand brand--right" style="left:372px; top:195px;"><span class="brand__small">gentle</span><span class="brand__caps">HUEWORK</span></div>
      <div class="hrule" style="left:150px; top:290px; width:370px;"></div>
      <p class="tagline" style="left:153px; top:303px; font-size:22px;">handmade with love in the USA</p>
      <p class="el regular" style="left:157px; top:330px; font-size:27px;">SMOOTH</p>
      <p class="el regular" style="left:314px; top:330px; font-size:27px;">COLOR</p>
      <p class="el bold" style="left:432px; top:327px; font-size:32px;">SET</p>
    </div>
    <div class="lid lid--clear">
      <div class="brand brand--right" style="left:332px; top:195px;"><span class="brand__small">gentle</span><span class="brand__caps">HUEWORK</span></div>
      <div class="hrule" style="left:117px; top:290px; width:370px;"></div>
      <p class="tagline" style="left:120px; top:303px; font-size:22px;">handmade with love in the USA</p>
      <p class="el regular" style="left:123px; top:332px; font-size:27px;">SMOOTH</p>
      <p class="el bold" style="left:268px; top:326px; font-size:36px;">COLOR</p>
      <p class="el regular" style="left:418px; top:330px; font-size:28px;">SET</p>
    </div>
  </section>

  <!-- Study 5: small lockup, short rule -->
  <section class="study">
    <div class="lid lid--black">
      <div class="brand" style="left:105px; top:246px;"><span class="brand__small">gentle</span><span class="brand__caps">HUEWORK</span></div>
      <div class="vrule" style="left:260px; top:240px; height:90px;"></div>
      <p class="tagline" style="left:274px; top:243px; font-size:15px;">handmade with love in the USA</p>
      <p class="el regular" style="left:274px; top:264px; font-size:30px;">SMOOTH</p>
      <p class="el regular" style="left:274px; top:296px; font-size:34px;">COLOR <span class="bold">SET</span></p>
    </div>
    <div class="lid lid--clear">
      <div class="brand" style="left:92px; top:246px;"><span class="brand__small">gentle</span><span class="brand__caps">HUEWORK</span></div>
      <div class="vrule" style="left:248px; top:240px; height:90px;"></div>
      <p class="tagline" style="left:262px; top:243px; font-size:15px;">handmade with love in the USA</p>
      <p class="el regular" style="left:262px; top:264px; font-size:30px;">SMOOTH</p>
      <p class="el bold" style="left:262px; top:296px; font-size:34px;">COLOR SET</p>
    </div>
  </section>

</main>
</body>
</html>
```